Business Card Design for Lawn Management

Lawn Management

Industry/Entity Type

Business

Contact Information for Business Card

Calloway Lawn Management
Doran Calloway
Calloway_Lawn@brindlemail.com
404-627-1845

```html
<!DOCTYPE html>
<html lang="en">
<head>
<meta charset="UTF-8">
<title>Calloway Lawn Management – Business Card</title>
<link rel="stylesheet" href="https://fonts.googleapis.com/css2?family=Exo+2:wght@400;500;600&display=swap">
<style>
  :root {
    --bg: #e9e9e7;
    --card-white: #ffffff;
    --green: #2f9a3f;
    --green-light: #46ad4f;
    --green-dark: #23852f;
    --stripe-grey: #9b9b9b;
    --text-on-green: #ffffff;
    --shadow: rgba(0,0,0,0.18);
  }
  html, body {
    margin: 0;
    width: 1200px;
    height: 900px;
    overflow: hidden;
    background: var(--bg);
  }
  .canvas {
    position: relative;
    width: 1200px;
    height: 900px;
  }
  .card {
    position: absolute;
    left: 100px;
    top: 164px;
    width: 1000px;
    height: 572px;
    border-radius: 46px;
    background: var(--card-white);
    overflow: hidden;
    box-shadow: 0 14px 36px var(--shadow);
    font-family: "Exo 2", sans-serif;
  }
  .card-shapes {
    position: absolute;
    inset: 0;
  }
  .brand {
    position: absolute;
    left: 92px;
    top: 236px;
    display: flex;
    align-items: center;
    gap: 16px;
    color: var(--green);
    font-weight: 600;
  }
  .brand-dot {
    width: 40px;
    height: 40px;
    border-radius: 50%;
    background: var(--green);
    flex: none;
  }
  .brand-name {
    font-size: 38px;
    line-height: 1.05;
    letter-spacing: 0.5px;
    text-transform: uppercase;
  }
  .brand-name span {
    display: block;
    font-size: 24px;
    text-transform: none;
  }
  .details {
    position: absolute;
    right: 58px;
    top: 60px;
    text-align: right;
    color: var(--text-on-green);
  }
  .person-name {
    font-size: 27px;
    font-weight: 500;
    letter-spacing: 1.5px;
    text-transform: uppercase;
    margin: 0;
  }
  .person-title {
    font-size: 17px;
    letter-spacing: 2px;
    text-transform: uppercase;
    margin: 4px 0 0;
  }
  .address {
    font-size: 21px;
    line-height: 1.3;
    margin: 58px 0 0;
    letter-spacing: 0.5px;
  }
  .contacts {
    list-style: none;
    margin: 40px 0 0;
    padding: 0;
    font-size: 19px;
    letter-spacing: 0.5px;
  }
  .contacts li {
    display: flex;
    justify-content: flex-end;
    align-items: center;
    gap: 12px;
    height: 32px;
  }
  .contact-icon { width: 20px; height: 20px; flex: none; }
</style>
</head>
<body>
<div class="canvas">
  <div class="card">
    <svg class="card-shapes" width="1000" height="572" viewBox="0 0 1000 572" aria-hidden="true">
      <defs>
        <radialGradient id="greenPanel" cx="0.55" cy="0.4" r="0.7">
          <stop offset="0" stop-color="#46ad4f"/>
          <stop offset="1" stop-color="#23852f"/>
        </radialGradient>
      </defs>
      <path class="grey-stripe" fill="var(--stripe-grey)"
            d="M250 0 C420 10 488 150 478 300 C470 420 450 500 420 572 L1000 572 L1000 0 Z"/>
      <path class="green-panel" fill="url(#greenPanel)"
            d="M278 0 C440 14 504 150 494 300 C486 420 466 500 438 572 L1000 572 L1000 0 Z"/>
    </svg>

    <div class="brand">
      <div class="brand-dot"></div>
      <div class="brand-name">Calloway<span>Lawn Management</span></div>
    </div>

    <div class="details">
      <p class="person-name">Doran Calloway</p>
      <p class="person-title">President</p>
      <p class="address">112, 9th floor, Elm Court<br>Birchfield Avenue</p>
      <ul class="contacts">
        <li>404-627-1845
          <svg class="contact-icon" viewBox="0 0 24 24" fill="#fff" aria-label="phone"><path d="M6.6 10.8a15 15 0 0 0 6.6 6.6l2.2-2.2c.3-.3.7-.4 1-.2 1.1.4 2.3.6 3.6.6.6 0 1 .4 1 1V20c0 .6-.4 1-1 1A17 17 0 0 1 3 4c0-.6.4-1 1-1h3.5c.6 0 1 .4 1 1 0 1.3.2 2.5.6 3.6.1.3 0 .7-.2 1z"/></svg>
        </li>
        <li>404-627-1845
          <svg class="contact-icon" viewBox="0 0 24 24" fill="none" stroke="#fff" stroke-width="2" aria-label="mobile"><rect x="6" y="2" width="12" height="20" rx="2"/><line x1="11" y1="18" x2="13" y2="18"/></svg>
        </li>
        <li>404-627-1845
          <svg class="contact-icon" viewBox="0 0 24 24" fill="#fff" aria-label="fax"><rect x="4" y="9" width="16" height="12" rx="1"/><rect x="7" y="3" width="10" height="6" fill="none" stroke="#fff" stroke-width="2"/></svg>
        </li>
        <li>Calloway_Lawn@brindlemail.com
          <svg class="contact-icon" viewBox="0 0 24 24" fill="#fff" aria-label="email"><path d="M2 5h20v14H2z"/><path d="M2 5l10 8 10-8" fill="none" stroke="#2f9a3f" stroke-width="1.6"/></svg>
        </li>
        <li>www.callowaylawn.com
          <svg class="contact-icon" viewBox="0 0 24 24" fill="none" stroke="#fff" stroke-width="1.8" aria-label="website"><circle cx="12" cy="12" r="9"/><ellipse cx="12" cy="12" rx="4" ry="9"/><line x1="3" y1="12" x2="21" y2="12"/></svg>
        </li>
      </ul>
    </div>
  </div>
</div>
</body>
</html>
```